Marrow Ridge Workforce Roundtable Event

Would like to have an e-postcard created that we can send out via email to recipients to invite them to the event. Also needs to include the Workforce Roundtable logo. I will upload the logo as well as information that needs to go on the e-postcard.

The Marrow Ridge Workforce Roundtable is a collaborative group with leaders such as City Managers, Chamber Directors, Education leaders, and Industry CEO's that work together to address industry needs in the community.

Target Market(s)

City Leaders, Company CEO's, Community Members, Elected Officials

Industry/Entity Type

Event

Requirements
Must have
• The invitation must be able to be sent via email to recipients
• Must include the Marrow Ridge Workforce Roundtable logo
• Be easy to read and understand
Nice to have
• Would like to see the incorporating of the following colors if possible: #0655a3; #0393ce; #00a990

```html
<!DOCTYPE html>
<html lang="en">
<head>
<meta charset="utf-8">
<title>Marrow Ridge Workforce Roundtable – Event Invitation</title>
<link rel="stylesheet" href="https://fonts.googleapis.com/css2?family=Source+Sans+3:wght@400;600;700&display=swap">
<style>
  :root {
    --navy: #0655a3;
    --sky: #0393ce;
    --teal: #00a990;
    --ink: #4a4a4c;
    --link: #1a3f9c;
    --page: #d1d2d4;
    --card: #ffffff;
    --figure-dark: #5f5f61;
    --figure-light: #eeeeef;
  }
  * { box-sizing: border-box; margin: 0; padding: 0; }
  html, body {
    width: 1200px; height: 1200px; overflow: hidden;
    background: var(--page);
    font-family: "Source Sans 3", "Myriad Pro", sans-serif;
  }
  .postcard {
    position: absolute; left: 40px; top: 236px;
    width: 1120px; height: 728px;
    background: var(--card);
    border: 6px solid var(--navy);
    box-shadow: 4px 6px 10px rgba(0,0,0,0.25);
  }
  .postcard-inner {
    position: absolute; inset: 14px;
    border: 2px solid var(--sky);
    overflow: hidden;
    background: linear-gradient(120deg, #ffffff 0%, #f7f7f8 45%, #eeeff0 70%, #f8f8f9 100%);
  }
  .date-banner {
    position: absolute; left: 0; top: 0;
    width: 518px; height: 61px;
    background: var(--sky);
    clip-path: polygon(0 0, 100% 0, 93% 100%, 0 100%);
    color: #fff; font-weight: 700; font-size: 29px;
    padding: 12px 0 0 59px;
  }
  .schedule {
    position: absolute; left: 54px; top: 104px;
    display: flex; font-size: 20px; line-height: 26px; color: var(--ink);
  }
  .schedule-icon { width: 48px; height: 48px; margin-right: 24px; margin-top: 2px; }
  .schedule-times { width: 196px; }
  .schedule-details { width: 260px; }
  .body-copy {
    position: absolute; left: 66px; width: 560px;
    font-size: 20px; line-height: 26px; color: var(--ink);
  }
  .intro { top: 290px; }
  .speakers { top: 421px; }
  .register { top: 553px; }
  .register-link { color: var(--link); text-decoration: none; display: block; }
  .deadline { color: var(--teal); font-weight: 700; font-size: 22px; }
  .brand {
    position: absolute; right: 44px; top: 58px;
    display: flex; align-items: center; gap: 14px;
  }
  .brand-mark { width: 40px; height: 40px; background: var(--navy); }
  .brand-name {
    color: var(--navy); font-weight: 600; font-size: 27px; line-height: 30px;
  }
  .team-illustration {
    position: absolute; left: 668px; top: 200px;
    width: 378px; height: 400px;
    background: linear-gradient(180deg, var(--figure-dark) 0%, var(--figure-dark) 62%, var(--figure-light) 100%);
    opacity: 0.55;
    border-radius: 6px;
  }
  .site-band {
    position: absolute; right: 0; bottom: 0;
    width: 464px; height: 55px;
    background: var(--teal);
    clip-path: polygon(9% 0, 100% 0, 100% 100%, 0 100%);
    color: #fff; font-weight: 700; font-size: 25px;
    padding: 11px 0 0 72px;
  }
</style>
</head>
<body>
  <article class="postcard">
    <div class="postcard-inner">
      <div class="date-banner">Thursday, November 3, 2016</div>

      <div class="brand">
        <span class="brand-mark"></span>
        <div class="brand-name">Marrow Ridge<br>Workforce Roundtable</div>
      </div>

      <div class="schedule">
        <svg class="schedule-icon" viewBox="0 0 48 48" aria-hidden="true">
          <circle cx="24" cy="27" r="16" fill="none" stroke="var(--teal)" stroke-width="4"/>
          <path d="M24 18v10l6 4" fill="none" stroke="var(--teal)" stroke-width="3.5" stroke-linecap="round"/>
          <path d="M5 12a8 8 0 0 1 10-8M43 12a8 8 0 0 0-10-8" fill="none" stroke="var(--teal)" stroke-width="4" stroke-linecap="round"/>
          <path d="M13 41l-3 4M35 41l3 4" stroke="var(--teal)" stroke-width="3.5" stroke-linecap="round"/>
        </svg>
        <div class="schedule-times">3:00pm – 5:00pm<br>5:00pm – 6:00pm</div>
        <div class="schedule-details">Program<br>Reception/Networking with light appetizers and no host bar Alder Alumni Center, Hartwell Ballroom</div>
      </div>

      <p class="body-copy intro">Please join us at an event highlighting the notable achievements to date as well as learn about work still to be accomplished. None of the successes could have occurred without the collective efforts and partnerships by many.</p>

      <p class="body-copy speakers">The Keynote Speaker will be Dana Halloway, incoming Mayor of Brookhaven. Other speakers include Nora Pell, Travel Marrow Ridge; Owen Tarrant, Regional Technology Alliance; and Ruth Calder, Valley Farm and Food Coalition.</p>

      <div class="body-copy register">
        <p>Please click the link to register for the event</p>
        <a class="register-link" href="#">http://www.marrowridgeworkforce.org/workforce-roundtable-event-november-3-2016/</a>
        <p class="deadline">Registration deadline is October 14, 2016.</p>
      </div>

      <div class="team-illustration" role="img" aria-label="Illustration of three business professionals standing side by side"></div>

      <div class="site-band">www.marrowridgeworkforce.org</div>
    </div>
  </article>
</body>
</html>
```